IT Company based on Biology Business Needs a Professional Web Design

We need a professional business website design for a new company called 'Vast KELP'. We develop the machine learning solutions especially focused on deep learning algorithms for biology industry. Our initial product is a vision detection on biological images to help doctors diagnose the symptoms. We would like to see designs that use the color green.

Industry/Entity Type

Business

Number of Pages Required

5+ page

```html
<!DOCTYPE html>
<html lang="en">
<head>
<meta charset="utf-8">
<title>Vast KELP — Vision Detection on Biological Images</title>
<link rel="stylesheet" href="https://fonts.googleapis.com/css2?family=Open+Sans:wght@300;400;600;700&display=swap">
<style>
:root{
  --green:#1f8a45;
  --green-dark:#17773a;
  --lime:#8cc63f;
  --cta:#7cc143;
  --ink:#2b2b2b;
  --text:#555;
  --muted:#777;
  --line:#e4e4e4;
  --pale:#f4f7fa;
  --navy:#1d3557;
  --footer:#f6f6f6;
}
*{margin:0;padding:0;box-sizing:border-box}
html,body{width:1200px;height:2839px;overflow:hidden}
body{font-family:"Open Sans",Arial,sans-serif;color:var(--text);background:#fff;position:relative}
.abs{position:absolute}

/* header */
.site-header{position:absolute;left:0;top:0;width:1200px;height:95px;background:#fff;border-bottom:1px solid var(--line)}
.site-header .topline{position:absolute;left:625px;top:0;width:575px;height:3px;background:var(--green)}
.brand{position:absolute;left:98px;top:30px;display:flex;align-items:center;gap:10px;font-size:24px;font-weight:600;color:var(--green);letter-spacing:.5px}
.brand .dot{width:16px;height:16px;border-radius:50%;background:var(--lime)}
.main-nav{position:absolute;top:38px;left:450px;display:flex;font-size:13.5px;color:#333}
.main-nav span{position:absolute;white-space:nowrap}
.main-nav .active{color:var(--green)}
.nav-mark{position:absolute;left:450px;top:64px;width:38px;height:10px}

/* hero */
.hero{position:absolute;left:0;top:95px;width:1200px;height:562px;background:linear-gradient(90deg,#b98a6e 0%,#6d6f78 30%,#3f5f86 55%,#7fb3d8 80%,#cfe6f5 100%)}
.hero-banner{position:absolute;left:100px;top:232px;width:536px;height:114px;background:rgba(31,138,69,.92);color:#fff;padding:12px 0 0 130px}
.hero-banner h1{font-size:42px;font-weight:700;line-height:46px;letter-spacing:.3px}
.hero-banner p{font-size:28px;font-weight:400;line-height:34px;letter-spacing:.4px}
.hero-banner .mark{position:absolute;left:34px;top:24px;width:66px;height:66px;border-radius:50%;background:#fff;opacity:.9}

/* section heads */
.sec-title{position:absolute;left:0;width:1200px;text-align:center;color:var(--ink);font-weight:400}
.sec-title em{font-style:normal;color:var(--green)}
.divider{position:absolute;left:562px;width:76px;height:12px}
.lead{position:absolute;left:163px;width:874px;text-align:center;font-size:11.5px;line-height:15.5px;color:var(--text)}

/* feature cards */
.feature{position:absolute;top:882px;width:281px;height:203px;background:#fff;border:1px solid #e8e8e8;border-bottom:3px solid #dcebd0;box-shadow:0 2px 6px rgba(0,0,0,.06);padding:22px 20px 0 52px}
.feature h3{font-size:17px;font-weight:400;color:#333;margin-bottom:12px}
.feature p{font-size:11.5px;line-height:20px;color:var(--text)}
.feature .btn{display:inline-block;margin-top:16px;border:1px solid var(--green);color:var(--green);font-size:12px;padding:4px 10px;border-radius:2px}
.feature-icon{position:absolute;left:-38px;top:54px;width:72px;height:72px;border-radius:50%;display:flex;align-items:center;justify-content:center}

/* algorithms */
.algo{position:absolute;left:0;top:1138px;width:1200px;height:467px;background:var(--pale);border-top:1px solid var(--line);border-bottom:1px solid var(--line)}
.algo-visual{position:absolute;left:0;top:0;width:547px;height:467px;background:linear-gradient(135deg,#eaf1f7,#dfe9f1);border-right:1px solid var(--line)}
.monitor{position:absolute;left:123px;top:55px;width:350px;height:330px;border-radius:10px;background:linear-gradient(160deg,#7fa9c6 0%,#2f5977 55%,#c9ced3 100%)}
.algo h2{position:absolute;left:608px;top:64px;font-size:30px;font-weight:400;color:var(--navy);letter-spacing:.5px}
.algo .body{position:absolute;left:608px;top:117px;width:430px;font-size:11.5px;line-height:19.5px;color:var(--text)}
.checks{position:absolute;left:608px;top:215px;list-style:none;font-size:12.5px;color:var(--text)}
.checks li{height:30px;display:flex;align-items:center;gap:12px}
.btn-solid{position:absolute;left:608px;top:348px;width:153px;height:40px;background:var(--green);color:#fff;font-size:12.5px;display:flex;align-items:center;justify-content:center;border-radius:2px;letter-spacing:.3px}

/* products */
.product{position:absolute;top:1793px;width:311px}
.product .thumb{width:311px;height:189px;border:3px solid #e3e3e3}
.product h4{margin-top:25px;font-size:17px;font-weight:400;color:#333}
.product p{margin-top:10px;font-size:11.5px;line-height:20px;color:var(--text)}
.product .more{display:inline-block;margin-top:16px;font-size:13px;color:#333;border-bottom:1px solid #333;line-height:16px}

/* cta */
.cta{position:absolute;left:0;top:2186px;width:1200px;height:351px;background:linear-gradient(180deg,#86c84a,#74ba3a);text-align:center;color:#fff}
.cta h2{position:absolute;left:0;width:1200px;top:114px;font-size:34px;font-weight:600;letter-spacing:.5px}
.cta p{position:absolute;left:0;width:1200px;top:160px;font-size:15px;color:#eef8e4}
.cta .ghost{position:absolute;left:526px;top:203px;width:138px;height:40px;border:1px solid #fff;border-radius:3px;font-size:12.5px;display:flex;align-items:center;justify-content:center;gap:8px}

/* footer */
.site-footer{position:absolute;left:0;top:2537px;width:1200px;height:246px;background:var(--footer)}
.foot-brand{position:absolute;left:98px;top:48px;font-size:20px;font-weight:600;color:var(--green);display:flex;align-items:center;gap:8px}
.foot-brand .dot{width:14px;height:14px;border-radius:50%;background:var(--lime)}
.foot-col h5{position:absolute;font-size:15px;font-weight:400;color:#333;letter-spacing:.3px}
.foot-col h5 em{font-style:normal;color:var(--green)}
.links{position:absolute;left:252px;top:68px;list-style:none;font-size:11.5px;color:#444;line-height:25.6px}
.news-copy{position:absolute;left:496px;top:68px;width:270px;font-size:11.5px;line-height:19px;color:var(--text)}
.field{position:absolute;left:496px;width:263px;height:42px;background:#fff;border:1px solid #e6e6e6;font-size:11.5px;color:#555;padding:12px 0 0 12px}
.subscribe{position:absolute;left:661px;top:170px;width:98px;height:40px;background:var(--green);color:#fff;font-size:12px;display:flex;align-items:center;justify-content:center}
.contact{position:absolute;left:869px;top:68px;font-size:12px;line-height:21px;color:var(--text)}
.contact-row{position:absolute;left:869px;display:flex;align-items:center;gap:14px;font-size:12.5px;color:#444}

.bottom-bar{position:absolute;left:0;top:2783px;width:1200px;height:56px;background:var(--green);color:#e9f5ec;font-size:11.5px}
.bottom-bar .copy{position:absolute;left:98px;top:19px}
.social{position:absolute;top:17px;width:22px;height:22px;border-radius:50%;background:#fff}
</style>
</head>
<body>

<header class="site-header">
  <div class="topline"></div>
  <div class="brand"><span class="dot"></span>Vast KELP</div>
  <nav class="main-nav">
    <span class="active" style="left:0">HOME</span>
    <span style="left:76px">ABOUT VAST</span>
    <span style="left:188px">OUR INITIAL PRODUCT</span>
    <span style="left:355px">VAST ALGORITHMS</span>
    <span style="left:502px">NEWS</span>
    <span style="left:572px">CONTACT US</span>
  </nav>
  <svg class="nav-mark" viewBox="0 0 38 10"><line x1="4" y1="5" x2="34" y2="5" stroke="#1f8a45" stroke-width="1.5"/><circle cx="4" cy="5" r="3" fill="#1f8a45"/><circle cx="34" cy="5" r="3" fill="#1f8a45"/></svg>
</header>

<section class="hero" role="img" aria-label="Scientist looking into a microscope with a blue DNA helix and molecule hexagons overlay">
  <svg class="abs" style="left:40px;top:265px" width="30" height="64" viewBox="0 0 30 64"><polyline points="26,4 4,32 26,60" fill="none" stroke="#fff" stroke-opacity=".7" stroke-width="2"/></svg>
  <div class="hero-banner">
    <span class="mark"></span>
    <h1>VISION DETECTION</h1>
    <p>ON BIOLOGICAL IMAGES</p>
  </div>
</section>

<h2 class="sec-title" style="top:698px;font-size:42px">Welcome To <em>Vast Kelp</em></h2>
<svg class="divider" style="top:755px" viewBox="0 0 76 12"><line x1="0" y1="6" x2="76" y2="6" stroke="#1f8a45" stroke-width="1.2"/><circle cx="10" cy="6" r="4" fill="#fff" stroke="#1f8a45" stroke-width="1.2"/><circle cx="38" cy="6" r="4" fill="#fff" stroke="#1f8a45" stroke-width="1.2"/><circle cx="66" cy="6" r="4" fill="#fff" stroke="#1f8a45" stroke-width="1.2"/></svg>
<p class="lead" style="top:782px">Lorem ipsum dolor sit amet, consectetur adipiscing elit, sed do eiusmod tempor incididunt ut labore et dolore magna aliqua. Ut enim ad minim veniam, quis nostrud exercitation ullamco laboris nisi ut aliquip ex ea commodo consequat. Duis aute irure dolor in reprehenderit in voluptate velit esse cillum dolore eu fugiat nulla pariatur. Excepteur sint occaecat cupidatat non proident, sunt in culpa qui officia deserunt mollit anim id est laborum</p>

<article class="feature" style="left:134px">
  <div class="feature-icon" style="background:var(--green)"><svg width="30" height="26" viewBox="0 0 30 26"><rect x="2" y="2" width="26" height="17" rx="2" fill="none" stroke="#fff" stroke-width="2"/><line x1="10" y1="24" x2="20" y2="24" stroke="#fff" stroke-width="2"/><line x1="15" y1="19" x2="15" y2="24" stroke="#fff" stroke-width="2"/></svg></div>
  <h3>Machine Learning</h3>
  <p>Nemo enim ipsam voluptatem quia voluptas sit aspernatur aut odit aut fugit, sed quia consequuntur magni dolores eos qui ratione</p>
  <span class="btn">Read More</span>
</article>
<article class="feature" style="left:477px">
  <div class="feature-icon" style="background:var(--lime)"><svg width="30" height="26" viewBox="0 0 30 26"><rect x="2" y="3" width="9" height="9" fill="none" stroke="#fff" stroke-width="2"/><rect x="19" y="14" width="9" height="9" fill="none" stroke="#fff" stroke-width="2"/><polyline points="11,7 23,7 23,14" fill="none" stroke="#fff" stroke-width="2"/></svg></div>
  <h3>Learning Algorithms</h3>
  <p>Nemo enim ipsam voluptatem quia voluptas sit aspernatur aut odit aut fugit, sed quia consequuntur magni dolores eos qui ratione</p>
  <span class="btn">Read More</span>
</article>
<article class="feature" style="left:820px">
  <div class="feature-icon" style="background:var(--green)"><svg width="28" height="28" viewBox="0 0 28 28"><circle cx="14" cy="9" r="6" fill="none" stroke="#fff" stroke-width="2"/><path d="M3 26c0-6 5-9 11-9s11 3 11 9" fill="none" stroke="#fff" stroke-width="2"/><line x1="14" y1="19" x2="14" y2="25" stroke="#fff" stroke-width="2"/><line x1="11" y1="22" x2="17" y2="22" stroke="#fff" stroke-width="2"/></svg></div>
  <h3>Doctors Diagnose</h3>
  <p>Nemo enim ipsam voluptatem quia voluptas sit aspernatur aut odit aut fugit, sed quia consequuntur magni dolores eos qui ratione</p>
  <span class="btn">Read More</span>
</article>

<section class="algo">
  <div class="algo-visual">
    <div class="monitor" role="img" aria-label="Desktop monitor showing a laboratory microscope slide image"></div>
  </div>
  <h2>DEEP LEARNING ALGORITHMS</h2>
  <p class="body">Lorem ipsum dolor sit amet, consectetur adipiscing elit, sed do eiusmod tempor incididunt ut labore et dolore magna aliqua. Ut enim ad minim veniam, quis nostrud exercitation ullamco laboris nisi ut aliquip ex ea commodo consequat. Duis aute irure dolor in reprehenderit in voluptate velit esse</p>
  <ul class="checks">
    <li><svg width="12" height="10" viewBox="0 0 12 10"><polyline points="1,5 4.5,8.5 11,1.5" fill="none" stroke="#1f8a45" stroke-width="2.2"/></svg>Nemo enim ipsam voluptatem quia voluptas sit aspernatur</li>
    <li><svg width="12" height="10" viewBox="0 0 12 10"><polyline points="1,5 4.5,8.5 11,1.5" fill="none" stroke="#1f8a45" stroke-width="2.2"/></svg>Nemo enim ipsam voluptatem quia voluptas</li>
    <li><svg width="12" height="10" viewBox="0 0 12 10"><polyline points="1,5 4.5,8.5 11,1.5" fill="none" stroke="#1f8a45" stroke-width="2.2"/></svg>Duis aute irure dolor in reprehenderit in voluptate</li>
    <li><svg width="12" height="10" viewBox="0 0 12 10"><polyline points="1,5 4.5,8.5 11,1.5" fill="none" stroke="#1f8a45" stroke-width="2.2"/></svg>Nemo enim ipsam voluptatem quia voluptas</li>
  </ul>
  <span class="btn-solid">READ MORE &nbsp;INFO</span>
</section>

<h2 class="sec-title" style="top:1662px;font-size:30px">OUR INITIAL PRODUCT</h2>
<svg class="divider" style="top:1707px" viewBox="0 0 76 12"><line x1="0" y1="6" x2="76" y2="6" stroke="#1f8a45" stroke-width="1.2"/><circle cx="10" cy="6" r="4" fill="#fff" stroke="#1f8a45" stroke-width="1.2"/><circle cx="38" cy="6" r="4" fill="#fff" stroke="#1f8a45" stroke-width="1.2"/><circle cx="66" cy="6" r="4" fill="#fff" stroke="#1f8a45" stroke-width="1.2"/></svg>
<p class="lead" style="top:1735px">Our initial product is a vision detection on biological images to help doctors diagnose the symptoms</p>

<article class="product" style="left:100px">
  <div class="thumb" role="img" aria-label="Gloved hand pipetting blue liquid into laboratory flasks" style="background:linear-gradient(135deg,#cfe8f5,#3f9fd0 60%,#1f6fa3)"></div>
  <h4>Nemo enim ipsam voluptatem</h4>
  <p>Lorem ipsum dolor sit amet, consectetur adipiscing elit, sed do eiusmod tempor incididunt ut labore et dolore magna aliqua. Ut enim ad minim veniam, quis</p>
  <span class="more">Read More</span>
</article>
<article class="product" style="left:447px">
  <div class="thumb" role="img" aria-label="Microscope stage with a sample slide under blue light" style="background:linear-gradient(135deg,#8fb9d4,#2d5a7a 55%,#6fa9cc)"></div>
  <h4>Nemo enim ipsam voluptatem</h4>
  <p>Lorem ipsum dolor sit amet, consectetur adipiscing elit, sed do eiusmod tempor incididunt ut labore et dolore magna aliqua. Ut enim ad minim veniam, quis</p>
  <span class="more">Read More</span>
</article>
<article class="product" style="left:793px">
  <div class="thumb" role="img" aria-label="Hand in a glove drawing a DNA double helix with molecule sketches" style="background:linear-gradient(135deg,#f2f2f2,#d9d9d9 60%,#e9e2dc)"></div>
  <h4>Nemo enim ipsam voluptatem</h4>
  <p>Lorem ipsum dolor sit amet, consectetur adipiscing elit, sed do eiusmod tempor incididunt ut labore et dolore magna aliqua. Ut enim ad minim veniam, quis</p>
  <span class="more">Read More</span>
</article>

<section class="cta">
  <h2>WE DEVELOP THE MACHINE LEARNING</h2>
  <p>solutions especially focused on deep learning algorithms for biology industry</p>
  <span class="ghost">READ MORE <svg width="12" height="12" viewBox="0 0 12 12"><circle cx="6" cy="6" r="6" fill="#fff"/><polyline points="5,3.5 7.5,6 5,8.5" fill="none" stroke="#7cc143" stroke-width="1.6"/></svg></span>
</section>

<footer class="site-footer">
  <div class="foot-brand"><span class="dot"></span>Vast KELP</div>
  <div class="foot-col">
    <h5 style="left:252px;top:34px">INFORMATION</h5>
    <ul class="links"><li>Home</li><li>Who We Are</li><li>Our Products</li><li>News</li><li>Contact</li></ul>
  </div>
  <div class="foot-col">
    <h5 style="left:496px;top:34px">SIGN UP FOR <em>NEWSLETTER</em></h5>
    <p class="news-copy">Join us today and start celebrate the life of your lost loved one.</p>
    <div class="field" style="top:117px">Enter Name</div>
    <div class="field" style="top:170px;width:166px">Enter Email</div>
    <span class="subscribe">SUBSCRIBE</span>
  </div>
  <div class="foot-col">
    <h5 style="left:869px;top:34px">CONTACT US</h5>
    <p class="contact">Vast Kelp<br>18 Harbor Lane, Suite 204,<br>Portmere, OR 97000, United States</p>
    <div class="contact-row" style="top:136px"><svg width="16" height="16" viewBox="0 0 16 16"><path d="M3 1.5l3 3-1.8 2a9 9 0 0 0 5.3 5.3l2-1.8 3 3-2 2C6.5 15 1 9.5 1.5 3.5z" fill="none" stroke="#1f8a45" stroke-width="1.4"/></svg>+1.555.010.4821</div>
    <div class="contact-row" style="top:164px"><svg width="16" height="12" viewBox="0 0 16 12"><rect x="1" y="1" width="14" height="10" fill="none" stroke="#1f8a45" stroke-width="1.4"/><polyline points="1,1 8,7 15,1" fill="none" stroke="#1f8a45" stroke-width="1.4"/></svg>sales@vastkelp.example</div>
  </div>
</footer>

<div class="bottom-bar">
  <span class="copy">© 2016 Vast Kelp | All Rights Reserved</span>
  <span class="social" style="left:985px"></span>
  <span class="social" style="left:1015px"></span>
  <span class="social" style="left:1045px"></span>
  <span class="social" style="left:1076px"></span>
</div>

</body>
</html>
```